Letterhead creation for military law attorney

I need letterhead design for my business. We are now only doing military law and need to change address, logo and vision. I like the idea of using an eagle or a jolly roger flag

Target Market(s)

Military Law Clients

Colors
3176b5
85abd2

Requirements
Must have
• We are defending people against the government
Nice to have
• Jolly Roger Flag

```html
<!DOCTYPE html>
<html lang="en">
<head>
<meta charset="utf-8">
<title>Hartwell Law, PLLC — Letterhead</title>
<link href="https://fonts.googleapis.com/css2?family=Open+Sans:wght@700&family=Montserrat:wght@400;700&display=swap" rel="stylesheet">
<style>
  :root {
    --brand-blue: #3483f0;
    --sky-blue: #88c2f2;
    --slate: #4a5759;
    --watermark: #e3e4e4;
    --paper: #ffffff;
    --ink-light: #ffffff;
  }
  html, body {
    margin: 0;
    padding: 0;
    overflow: hidden;
    background: var(--paper);
  }
  .letterhead {
    position: relative;
    width: 902px;
    height: 1200px;
    overflow: hidden;
    background: var(--paper);
  }
  .top-band {
    position: absolute;
    top: 19px;
    left: 0;
    width: 902px;
    height: 45px;
    display: flex;
  }
  .top-band__primary { width: 451px; background: var(--brand-blue); }
  .top-band__secondary { flex: 1; background: var(--sky-blue); }

  .brand {
    position: absolute;
    top: 104px;
    left: 46px;
    display: flex;
    align-items: center;
    gap: 22px;
  }
  .brand__mark {
    width: 110px;
    height: 110px;
    border-radius: 50%;
    background: var(--slate);
  }
  .brand__name {
    margin: 0;
    font-family: "Open Sans", sans-serif;
    font-weight: 700;
    font-size: 48px;
    letter-spacing: 2.5px;
    color: var(--brand-blue);
    line-height: 1;
  }

  .doc-fields {
    position: absolute;
    top: 256px;
    left: 666px;
    width: 173px;
    font-family: "Montserrat", sans-serif;
    font-size: 17px;
    color: var(--slate);
  }
  .doc-field {
    display: flex;
    align-items: flex-end;
    height: 24px;
    margin-bottom: 18px;
  }
  .doc-field__rule {
    flex: 1;
    border-bottom: 1.5px solid var(--slate);
    margin-left: 2px;
    margin-bottom: 4px;
  }

  .flag-watermark {
    position: absolute;
    left: 400px;
    top: 392px;
    width: 502px;
    height: 742px;
    border-radius: 48% 0 0 40%;
    background: radial-gradient(ellipse at 70% 45%, var(--watermark) 0%, var(--watermark) 45%, rgba(227,228,228,0.35) 75%, rgba(255,255,255,0) 100%);
  }

  .footer-art {
    position: absolute;
    left: 0;
    top: 1057px;
    width: 902px;
    height: 143px;
  }

  .contact-icons {
    position: absolute;
    top: 1084px;
    left: 702px;
    display: flex;
    gap: 17px;
  }
  .contact-icon {
    width: 32px;
    height: 32px;
  }

  .contact-lines {
    position: absolute;
    right: 10px;
    top: 1120px;
    margin: 0;
    font-family: "Montserrat", sans-serif;
    font-weight: 700;
    font-size: 15px;
    letter-spacing: 1.3px;
    line-height: 19px;
    text-align: right;
    color: var(--ink-light);
    font-style: normal;
  }
</style>
</head>
<body>
<div class="letterhead">
  <div class="top-band">
    <div class="top-band__primary"></div>
    <div class="top-band__secondary"></div>
  </div>

  <header class="brand">
    <div class="brand__mark"></div>
    <h1 class="brand__name">HARTWELL LAW, PLLC</h1>
  </header>

  <div class="doc-fields">
    <div class="doc-field"><span>Ref:</span><span class="doc-field__rule"></span></div>
    <div class="doc-field"><span>Date:</span><span class="doc-field__rule"></span></div>
  </div>

  <div class="flag-watermark" role="img" aria-label="Faint grey Jolly Roger skull and crossbones watermark"></div>

  <svg class="footer-art" viewBox="0 0 902 143" aria-hidden="true">
    <rect x="0" y="98" width="570" height="45" fill="var(--brand-blue)"/>
    <polygon points="650,0 902,0 902,143 507,143" fill="var(--slate)"/>
  </svg>

  <div class="contact-icons">
    <svg class="contact-icon" viewBox="0 0 32 32" role="img" aria-label="Address">
      <circle cx="16" cy="16" r="15" fill="none" stroke="var(--brand-blue)" stroke-width="1.5"/>
      <path d="M16 7a6 6 0 0 0-6 6c0 4.5 6 11.5 6 11.5s6-7 6-11.5a6 6 0 0 0-6-6z" fill="var(--ink-light)"/>
      <circle cx="16" cy="13" r="2.2" fill="var(--slate)"/>
    </svg>
    <svg class="contact-icon" viewBox="0 0 32 32" role="img" aria-label="Phone">
      <circle cx="16" cy="16" r="15" fill="none" stroke="var(--brand-blue)" stroke-width="1.5"/>
      <path d="M10.5 9.5l3 -1 2 4.5-2 1.5c.8 2 2.2 3.4 4 4.2l1.5-2 4.5 2-1 3c-6 .5-12.5-6-12-12.2z" fill="var(--ink-light)"/>
      <path d="M18 9a5 5 0 0 1 5 5M18 6a8 8 0 0 1 8 8" fill="none" stroke="var(--ink-light)" stroke-width="1.3"/>
    </svg>
    <svg class="contact-icon" viewBox="0 0 32 32" role="img" aria-label="Fax">
      <circle cx="16" cy="16" r="15" fill="none" stroke="var(--brand-blue)" stroke-width="1.5"/>
      <rect x="11" y="7.5" width="10" height="6" fill="var(--ink-light)"/>
      <rect x="8" y="13" width="16" height="8" rx="1.5" fill="var(--ink-light)"/>
      <rect x="11" y="19" width="10" height="5.5" fill="var(--ink-light)" stroke="var(--slate)" stroke-width="1"/>
      <line x1="12.5" y1="9.5" x2="19.5" y2="9.5" stroke="var(--slate)" stroke-width="0.8"/>
      <line x1="12.5" y1="11.5" x2="19.5" y2="11.5" stroke="var(--slate)" stroke-width="0.8"/>
    </svg>
  </div>

  <address class="contact-lines">
    (555)014-2670<br>
    Fax: (555)014-2671<br>
    PO Box 318 Millbrook, TN 38002
  </address>
</div>
</body>
</html>
```